依頼詳細
現在、お店のロゴはあります。既存のロゴを使用して、立て看板を新しくしたいと思っています。看板の入稿に必要なデザインをillustratorで作成して頂きたいと思います。
重視するポイントは、
1。概要、特徴にも記載しましたが2Fとわかること。
2.ワインはそうですが、お食事ができること。
3.現在使用しているロゴを看板の中心にもっていってワインと一目でわかるようにしたい
4.現在の立て看板がとてもカジュアルな為、店内の雰囲気とかなりギャップがあります。若年の方が立ち飲みバルや、居酒屋、カフェ等と間違えて誤って入ってこられることがたまにあります。お店の雰囲気がでるようなシンプルで雰囲気のあるデザインを希望します。看板製作会社が、完全データの支給を要求しているため、Adobe Illustratorアウトラインデータ Mac=8.0 Win=CSにて納品お願いします。
お店の雰囲気、現在の看板、ロゴなどは添付ファイル参照ください。
記載項目
店舗名、2F、ワインとお食事、今のロゴ。定番メニューのリスト、電話番号。席数。
希望イメージ
シンプル 複雑
単色 カラフル
暗い 明るい
日常 高級
遊び心 厳粛
未来的 伝統的
女性的 男性的
希望する色
白、ワインレッド系、ロゴに合わせたカラー
納品ファイル
• 高解像度JPG (.jpg)
• イラストレーター形式 (.ai)
補足説明
入口の間口が狭いために、看板に必ず2F+↑を記載していただきたいです。表、左上がり、裏、右上がりの☝をつけてほしいです。現在の立て看板ファイルを参照してください。
看板仕上がりサイズはW600×H900です。【画面有効サイズ】 W530×H830mmとなっています。内側に投光機を設置し、ライトアップされます。宜しくお願いいたします。
■ 選んだ理由

現在の問題点をクリアし、お店の雰囲気が看板一つで出ている所。

■ 提案者全員のお礼・コメント

修正等にご対応いただきまして誠にありがとうございました。今後も名刺の修正等依頼していくつもりですので機会がありましたら是非とも宜しくお願いいたします。

```html
<!DOCTYPE html>
<html lang="ja">
<head>
<meta charset="utf-8">
<title>VERRE 立て看板</title>
<link href="https://fonts.googleapis.com/css2?family=Noto+Serif+JP:wght@400;500;600&family=Noto+Sans+JP:wght@400;500&family=Cormorant+Garamond:wght@500;600&display=swap" rel="stylesheet">
<style>
  :root {
    --frame: #a9aaac;
    --paper: #ffffff;
    --wine: #c0161d;
    --wine-deep: #9e1016;
    --brown: #4b2b1d;
    --ink: #2f2520;
    --on-dark: #ffffff;
  }
  * { margin: 0; padding: 0; box-sizing: border-box; }
  html, body { width: 798px; height: 1200px; overflow: hidden; background: var(--frame); }
  .signboard {
    position: relative;
    width: 798px; height: 1200px;
    background: var(--frame);
    padding: 30px;
  }
  .panel {
    position: relative;
    width: 100%; height: 100%;
    background: var(--paper);
    overflow: hidden;
  }
  .floor-mark {
    position: absolute; left: 30px; top: 10px;
    width: 300px; height: 320px;
  }
  .floor-badge {
    position: absolute; left: 47px; top: 50px;
    width: 250px; height: 250px; border-radius: 50%;
    background: var(--wine);
    color: var(--on-dark);
    font-family: "Noto Serif JP", serif; font-weight: 500;
    font-size: 150px; line-height: 250px; text-align: center;
    letter-spacing: -6px;
  }
  .floor-arrow { position: absolute; left: 0; top: 0; width: 110px; height: 110px; }
  .intro {
    position: absolute; left: 370px; top: 20px;
    font-family: "Noto Serif JP", serif; font-weight: 500;
    font-size: 31px; line-height: 50px; color: var(--ink);
    letter-spacing: 1px;
  }
  .glass-art {
    position: absolute; left: 40px; top: 340px;
    width: 120px; height: 270px;
    background: linear-gradient(180deg, #c0161d 0%, #8a4a35 60%, #6b4a35 100%);
    opacity: .85; border-radius: 8px;
  }
  .tagline {
    position: absolute; left: 330px; top: 340px;
    font-family: "Noto Serif JP", serif; font-weight: 500;
    font-size: 34px; color: var(--wine); letter-spacing: 2px;
  }
  .shop-name {
    position: absolute; left: 190px; top: 380px;
    font-family: "Cormorant Garamond", serif; font-weight: 600;
    font-size: 150px; line-height: 150px; color: var(--ink);
    letter-spacing: 8px;
  }
  .genre {
    position: absolute; left: 370px; top: 528px;
    font-family: "Noto Serif JP", serif; font-weight: 500;
    font-size: 34px; color: var(--ink); letter-spacing: 3px;
  }
  .info-band { position: absolute; left: 0; top: 585px; width: 100%; height: 230px; }
  .info-band svg { position: absolute; inset: 0; }
  .info-text {
    position: absolute; left: 26px; top: 60px;
    font-family: "Noto Sans JP", sans-serif; font-weight: 400;
    color: var(--on-dark);
  }
  .seats { font-size: 36px; line-height: 52px; letter-spacing: 1px; }
  .tel { font-size: 40px; line-height: 54px; letter-spacing: 2px; }
  .menu-area {
    position: absolute; left: 0; top: 800px; width: 100%; height: 340px;
    background: var(--brown);
  }
  .menu-list {
    position: absolute; left: 30px; top: 28px;
    list-style: none;
    font-family: "Noto Sans JP", sans-serif; font-weight: 400;
    font-size: 24px; line-height: 43px; color: var(--on-dark);
  }
  .menu-emblem {
    position: absolute; left: 548px; top: 20px;
    width: 170px; height: 170px; border-radius: 50%;
    background: radial-gradient(circle, #7a5a48 0%, #5e3d2c 100%);
  }
</style>
</head>
<body>
<div class="signboard">
  <div class="panel">
    <div class="floor-mark">
      <div class="floor-badge">2F</div>
      <svg class="floor-arrow" viewBox="0 0 110 110" aria-label="上階への矢印">
        <rect x="0" y="0" width="110" height="110" fill="#2f2520"/>
        <path d="M20 20 L70 20 L54 36 L92 74 L74 92 L36 54 L20 70 Z" fill="#ffffff"/>
      </svg>
    </div>

    <p class="intro">近場の築地市場にて<br>旬の食材を仕入れ<br>ワインに合うお食事を<br>日替わりにて<br>ご用意しております。</p>

    <div class="glass-art" role="img" aria-label="ワイングラスのイラスト"></div>
    <p class="tagline">WINE &amp; DINE</p>
    <h1 class="shop-name">VERRE</h1>
    <p class="genre">ワインとお食事</p>

    <div class="info-band">
      <svg viewBox="0 0 738 230" preserveAspectRatio="none">
        <path d="M0 40 C180 0 520 0 738 30 L738 230 L0 230 Z" fill="var(--wine)"/>
      </svg>
      <div class="info-text">
        <p class="seats">カウンター［7席］・テーブル［10席］</p>
        <p class="tel">TEL.090-4821-7365</p>
      </div>
    </div>

    <div class="menu-area">
      <ul class="menu-list">
        <li>グラスワイン（白・赤）各種</li>
        <li>グラススパークリング・ボトル各種</li>
        <li>秋刀魚のアクア・パッツア</li>
        <li>牛サーロインのステーキ、フレンチフライ添え</li>
        <li>ポークと野菜の南イタリア風煮込 etc.</li>
      </ul>
      <div class="menu-emblem" role="img" aria-label="ナイフとフォークに手書きのMenu文字の紋章"></div>
    </div>
  </div>
</div>
</body>
</html>
```